Modern Business Card

Modern professional business card with more than just logo and demographic info. Something memorable.

We are a trendy/modern chiropractic group with an emphasis on neurology, hence the minimalist-type brain logo. We want to convey that modern and technical aspect with professionalism and the elite nature of our practice environment.

```html
<!DOCTYPE html>
<html lang="en">
<head>
<meta charset="utf-8">
<title>Veritas Spine – Business Card</title>
<link href="https://fonts.googleapis.com/css2?family=Roboto:wght@300;400;500&display=swap" rel="stylesheet">
<style>
  :root {
    --page: #e9e9ea;
    --card: #262626;
    --card-deep: #151515;
    --pattern-mid: #333333;
    --pattern-light: #575757;
    --accent: #4a7fd0;
    --ink: #f2f2f2;
    --rule: #6a6a6a;
  }
  * { box-sizing: border-box; margin: 0; padding: 0; }
  html, body {
    width: 1200px; height: 801px; overflow: hidden;
    background: var(--page);
    font-family: "Roboto", Arial, sans-serif;
  }
  .sheet {
    position: relative; width: 1200px; height: 801px;
    display: flex; align-items: center; justify-content: center; gap: 48px;
  }
  .card {
    position: relative; width: 525px; height: 300px;
    background: var(--card);
    border-bottom: 4px solid var(--accent);
    box-shadow: 0 10px 24px rgba(0,0,0,.18);
    overflow: hidden;
  }
  /* front */
  .brand {
    position: absolute; top: 58px; left: 0; right: 0;
    display: flex; align-items: center; justify-content: center; gap: 14px;
  }
  .brand-dot { width: 42px; height: 42px; background: var(--accent); border-radius: 50%; }
  .brand-name {
    color: var(--ink); font-weight: 400; font-size: 32px; letter-spacing: 2px;
    text-transform: uppercase; line-height: 1;
  }
  .details {
    position: absolute; top: 146px; left: 0; right: 0;
    display: flex; justify-content: center; align-items: center;
  }
  .person { text-align: right; padding-right: 20px; }
  .person-name { color: var(--accent); font-size: 22px; font-weight: 400; }
  .person-role { color: var(--ink); font-size: 16px; font-weight: 300; margin-top: 2px; }
  .divider { width: 1px; height: 70px; background: var(--rule); }
  .contact { list-style: none; padding-left: 20px; }
  .contact li {
    color: var(--ink); font-size: 14px; font-weight: 300; line-height: 22px;
    display: flex; align-items: center; gap: 9px;
  }
  .contact svg { width: 12px; height: 12px; flex: none; }
  .contact .web-domain { color: var(--accent); }
  .address {
    position: absolute; bottom: 42px; left: 0; right: 0; text-align: center;
    color: var(--ink); font-size: 15px; font-weight: 300;
  }
  /* back */
  .back-texture {
    position: absolute; inset: 0;
    background: linear-gradient(125deg,
      var(--card-deep) 0%,
      var(--card-deep) 22%,
      var(--pattern-mid) 48%,
      var(--card) 58%,
      var(--pattern-light) 82%,
      var(--pattern-mid) 100%);
  }
  .back-mark {
    position: absolute; right: 92px; bottom: 72px;
    width: 36px; height: 36px; background: var(--accent);
  }
</style>
</head>
<body>
<main class="sheet">
  <section class="card card-front">
    <div class="brand">
      <span class="brand-dot"></span>
      <span class="brand-name">Veritas Spine</span>
    </div>
    <div class="details">
      <div class="person">
        <p class="person-name">Daniel Brooks</p>
        <p class="person-role">Manager</p>
      </div>
      <span class="divider"></span>
      <ul class="contact">
        <li>
          <svg viewBox="0 0 12 12"><path d="M2 1l2 0 1 3-1.5 1a6 6 0 0 0 3.5 3.5L8 7l3 1v2a1 1 0 0 1-1 1A9 9 0 0 1 1 2a1 1 0 0 1 1-1z" fill="var(--accent)"/></svg>
          555-018-2100
        </li>
        <li>
          <svg viewBox="0 0 12 12"><rect x="0.8" y="2.3" width="10.4" height="7.4" fill="none" stroke="var(--accent)" stroke-width="1.2"/><path d="M1 2.8l5 3.8 5-3.8" fill="none" stroke="var(--accent)" stroke-width="1.2"/></svg>
          hello@veritasspine.com
        </li>
        <li>
          <svg viewBox="0 0 12 12"><circle cx="6" cy="6" r="5.2" fill="none" stroke="var(--accent)" stroke-width="1.1"/><path d="M1 6h10M6 1c-2.5 3-2.5 7 0 10M6 1c2.5 3 2.5 7 0 10" fill="none" stroke="var(--accent)" stroke-width="1"/></svg>
          <span>www.<span class="web-domain">veritasspine</span>.com</span>
        </li>
      </ul>
    </div>
    <p class="address">Your address, city, state, ZIP 0000</p>
  </section>

  <section class="card card-back">
    <div class="back-texture" role="img" aria-label="Repeating embossed pattern of the practice's brain symbol in dark greys, lighter toward the right, filling the whole back of the card"></div>
    <span class="back-mark"></span>
  </section>
</main>
</body>
</html>
```